Templates for Construction Company

We are looking to have templates prepared for all aspects of our letter sending. Using our brand design. with similar layouts that look the same.

Letterheads design & Email signatures

We use letter heads for - quotes, contract correspondence, variations, formal letters, invitations

Target Market(s)

Clients documents sent in emails

Industry/Entity Type

Construction

Font styles to use
Serif
Sans Serif

Colors
0054AA
0677BA
7BADD7
CADEEF
E8F1F8

Requirements
Must have
• Easy to read, water marks on page
Nice to have
• Different options for different letters

```html
<!DOCTYPE html>
<html lang="en">
<head>
<meta charset="utf-8">
<title>Framewell Construction Group – Stationery</title>
<link href="https://fonts.googleapis.com/css2?family=Montserrat:wght@400;500;700&display=swap" rel="stylesheet">
<style>
  :root{
    --brand-blue:#589cfb;
    --brand-navy:#1f4fc8;
    --slate:#56646a;
    --paper:#ffffff;
    --ink:#1d1d1f;
    --backdrop:#d6dddc;
    --sign-fill:#e4e9ec;
  }
  *{box-sizing:border-box;margin:0;padding:0}
  html,body{width:1200px;height:856px;overflow:hidden}
  body{background:var(--backdrop);font-family:"Montserrat",Arial,sans-serif;color:var(--ink);position:relative}

  /* ---------- Email signature ---------- */
  .email-signature{position:absolute;left:67px;top:313px;width:549px;height:222px;background:var(--paper)}
  .email-signature .shapes,.letterhead .shapes{position:absolute;inset:0;width:100%;height:100%}
  .brand{position:absolute;display:flex;align-items:flex-start;gap:6px}
  .brand-square{width:9px;height:9px;background:var(--slate);margin-top:8px}
  .brand-name{font-weight:700;color:var(--brand-blue);line-height:1}
  .brand-tagline{font-weight:500;color:var(--slate);letter-spacing:.04em;margin-top:3px;border-top:1px solid var(--brand-blue);padding-top:2px}
  .email-signature .brand{left:40px;top:96px}
  .email-signature .brand-name{font-size:25px}
  .email-signature .brand-tagline{font-size:6px}
  .social-links{position:absolute;left:82px;top:157px;display:flex;gap:16px}
  .social-dot{width:14px;height:14px;border-radius:50%;background:var(--brand-blue)}
  .signature-divider{position:absolute;left:226px;top:38px;width:1px;height:143px;background:var(--brand-blue)}
  .contact-icons{position:absolute;left:248px;top:47px;display:flex;flex-direction:column;gap:6px}
  .contact-icons svg{width:18px;height:18px;display:block}

  /* ---------- Letterhead ---------- */
  .letterhead{position:absolute;left:701px;top:141px;width:401px;height:567px;background:var(--paper)}
  .letterhead .brand{left:143px;top:80px}
  .letterhead .brand-name{font-size:28px}
  .letterhead .brand-tagline{font-size:5.6px}
  .letter-headline{position:absolute;left:39px;top:184px;font-size:18px;font-weight:700;color:var(--brand-navy)}
  .letter-body{position:absolute;left:39px;top:214px;width:310px;font-size:5.6px;line-height:12px}
  .letter-body p+p{margin-top:12px}
  .letter-signature{position:absolute;left:146px;top:434px;width:115px;height:30px;background:var(--sign-fill);border-radius:2px}
  .letter-address{position:absolute;left:19px;top:491px;display:flex;gap:5px;color:#fff;font-size:7px;line-height:10px}
  .letter-address svg{width:7px;height:9px;margin-top:1px}
</style>
</head>
<body>

<section class="email-signature" aria-label="Email signature">
  <svg class="shapes" viewBox="0 0 820 332" preserveAspectRatio="none" aria-hidden="true">
    <polygon points="0,0 42,168 82,332 0,332" fill="var(--brand-blue)"/>
    <polygon points="0,0 104,0 42,168" fill="var(--slate)"/>
    <polygon points="738,0 820,0 820,332 780,162" fill="var(--brand-blue)"/>
    <polygon points="780,162 820,332 718,332" fill="var(--slate)"/>
  </svg>

  <div class="brand">
    <span class="brand-square"></span>
    <div>
      <div class="brand-name">Framewell</div>
      <div class="brand-tagline">CONSTRUCTION GROUP</div>
    </div>
  </div>

  <div class="social-links">
    <span class="social-dot" aria-label="Social profile"></span>
    <span class="social-dot" aria-label="Social profile"></span>
    <span class="social-dot" aria-label="Social profile"></span>
  </div>

  <div class="signature-divider"></div>

  <div class="contact-icons">
    <svg viewBox="0 0 20 20" aria-label="Phone"><circle cx="10" cy="10" r="10" fill="var(--slate)"/><path d="M6.5 5.5l2 -.5 1 2.5-1.2 1a6 6 0 0 0 3.2 3.2l1-1.2 2.5 1-.5 2c-4.5.3-8.3-3.5-8-8z" fill="#fff"/></svg>
    <svg viewBox="0 0 20 20" aria-label="Fax"><circle cx="10" cy="10" r="10" fill="var(--slate)"/><rect x="7" y="4.5" width="6" height="3.5" fill="none" stroke="#fff" stroke-width="1.2"/><rect x="5" y="8" width="10" height="5" rx="1" fill="none" stroke="#fff" stroke-width="1.2"/><rect x="7" y="11.5" width="6" height="4" fill="var(--slate)" stroke="#fff" stroke-width="1.2"/></svg>
    <svg viewBox="0 0 20 20" aria-label="Email"><circle cx="10" cy="10" r="10" fill="var(--slate)"/><rect x="5" y="6.5" width="10" height="7" fill="none" stroke="#fff" stroke-width="1.2"/><polyline points="5,6.5 10,10.5 15,6.5" fill="none" stroke="#fff" stroke-width="1.2"/></svg>
    <svg viewBox="0 0 20 20" aria-label="Address"><circle cx="10" cy="10" r="10" fill="var(--slate)"/><path d="M10 4.5a3.8 3.8 0 0 0-3.8 3.8c0 2.8 3.8 7.2 3.8 7.2s3.8-4.4 3.8-7.2A3.8 3.8 0 0 0 10 4.5z" fill="#fff"/><circle cx="10" cy="8.3" r="1.4" fill="var(--slate)"/></svg>
    <svg viewBox="0 0 20 20" aria-label="Website"><circle cx="10" cy="10" r="10" fill="var(--slate)"/><g fill="none" stroke="#fff" stroke-width="1"><circle cx="10" cy="10" r="5.5"/><ellipse cx="10" cy="10" rx="2.4" ry="5.5"/><line x1="4.5" y1="10" x2="15.5" y2="10"/><line x1="5.3" y1="7.3" x2="14.7" y2="7.3"/><line x1="5.3" y1="12.7" x2="14.7" y2="12.7"/></g></svg>
  </div>
</section>

<section class="letterhead" aria-label="Letterhead">
  <svg class="shapes" viewBox="0 0 600 848" preserveAspectRatio="none" aria-hidden="true">
    <polygon points="0,0 598,0 295,77 0,148" fill="var(--brand-blue)"/>
    <polygon points="295,77 600,0 600,187" fill="var(--slate)"/>
    <polygon points="0,660 500,848 0,848" fill="var(--slate)"/>
  </svg>

  <div class="brand">
    <span class="brand-square"></span>
    <div>
      <div class="brand-name">Framewell</div>
      <div class="brand-tagline">CONSTRUCTION GROUP</div>
    </div>
  </div>

  <h1 class="letter-headline">HEADLINE</h1>

  <div class="letter-body">
    <p>This is a sample letter that has been placed to demonstrate typing format (Your Company). letterhead design. When positioned properly, it will serve to work in harmony with all other elements letterhead. This letterhead design is meant to project an image</p>
    <p>This letterhead design is meant project an image of professionalism reliability. By using simple alignment we have created a very spacious feeling. The simplicity suggests strength the spaciousness contributes to aesthetics the layout. These basic qualities along with the (Your Company)</p>
    <p>look and helps reinforce the (Your Company) brand. letterhead design is meant to project an image of design. When positioned properly, it will serve to work in harmony all the other elements letterhead. professionalism and reliability.</p>
    <p>This letterhead design is based on the (Form of your logo) form (Your Company) logo. Each stationery we have created a very spacious feeling. The simplicity suggests strength the spaciousness contribute part of the (Form of your logo).</p>
  </div>

  <div class="letter-signature" role="img" aria-label="Handwritten signature of Owen Carter"></div>

  <div class="letter-address">
    <svg viewBox="0 0 14 18" aria-hidden="true"><path d="M7 0a6.5 6.5 0 0 0-6.5 6.5C.5 11.3 7 18 7 18s6.5-6.7 6.5-11.5A6.5 6.5 0 0 0 7 0z" fill="#fff"/><circle cx="7" cy="6.5" r="2.3" fill="var(--slate)"/></svg>
    <div>your address<br>your address</div>
  </div>
</section>

</body>
</html>
```